Zertifikat-Design für Bildungsträger im Bereich der Erwachsenenbildung
Zielgruppe
Talwerk Akademie - Zertifizierter Bildungsträger im Bereich der Erwachsenenbildung. Überwiegend Mitarbeiter in Unternehmen.
Aufgabenstellung
'Erstelle ein hochwertiges, modernes und exklusiv wirkendes Zertifikat für die Talwerk Akademie. Das Design soll professionell, minimalistisch und zugleich edel sein. Ziel ist es, ein Dokument zu gestalten, das den Eindruck vermittelt: 'Das ist das einzige und beste Zertifikat in der ganzen verdammten Welt.'
Das Zertifikat soll im Querformat (idealerweise DIN A4 horizontal) gestaltet werden. Der Inhalt soll zweisprachig (Deutsch und Englisch) dargestellt werden, klar gegliedert und typografisch hochwertig aufgebaut. Alle Inhalte sollten mittig ausgerichtet sein, mit gut erkennbarer visueller Hierarchie.
Der Haupttext lautet wie folgt:
'Talwerk Akademie gratuliert 'Name / Platzhalter' zum erfolgreichen Abschluss des Kurses 'Platzhalter' Datum, Unterschrift (siehe unten)
+englisch
'Talwerk Akademie hereby certifies that [Name of Participant / Placeholder] has successfully participated on 'date'.
Darunter sollen zwei stilisierte Unterschriften platziert werden – gerne von Hand gezeichnet oder elegant typografisch umgesetzt. Die Beschriftung unter den Unterschriften lautet: 'Leitung Talwerk Akademie'.
Ein zentrales Element ist das Hologramm. Muster das gelieferte Bild 'Hologramm.png'. Es muss deutlich sichtbar und hochwertig integriert werden. Die Aufschrift 'Talwerk' im Hologramm muss klar erkennbar sein. Idealer Platz wäre unten links oder rechts, eventuell mit einer leichten 3D-Anmutung oder Glanzeffekt.
Das gesamte Design muss der Corporate Identity der Talwerk Akademie entsprechen. Die verwendeten Farben sind: Hauptfarbe Dunkelblau (RGB 14, 32, 62), ergänzt durch Hellblau (RGB 241, 245, 250), ein zusätzliches Blau (RGB 65, 111, 174), Pink (RGB 140, 130, 227), Dunkellila (RGB 169, 97, 161), sowie Gelb (RGB 248, 216, 73) und Orange (RGB 220, 121, 70) für gezielte Akzente.
Als Schriftart ist ausschließlich Roboto zu verwenden. Der Name des Teilnehmers soll besonders hervorgehoben werden (z...

```html
<!DOCTYPE html>
<html lang="de">
<head>
<meta charset="utf-8">
<title>Teilnahmezertifikat – Talwerk Akademie</title>
<link rel="stylesheet" href="https://fonts.googleapis.com/css2?family=Roboto:wght@300;400;700;900&family=Kaushan+Script&display=swap">
<style>
  :root {
    --navy: #0e203e;
    --lilac: #8882c0;
    --frame: #8884c0;
    --blue: #416fae;
    --rule: #c9c6e6;
    --ink: #000000;
    --paper: #ffffff;
  }
  * { margin: 0; padding: 0; box-sizing: border-box; }
  html, body { width: 1200px; height: 849px; overflow: hidden; background: var(--paper); }
  body { font-family: "Roboto", sans-serif; color: var(--navy); }
  .certificate { position: relative; width: 1200px; height: 849px; }
  .frame { position: absolute; inset: 0; }
  .line { position: absolute; left: 0; width: 1200px; text-align: center; line-height: 1; white-space: nowrap; }
  .title-de, .title-en { font-weight: 300; font-size: 34px; letter-spacing: 0.3em; padding-left: 0.3em; }
  .title-de { top: 99px; color: var(--navy); }
  .title-en { top: 142px; color: var(--lilac); }
  .academy { top: 243px; font-weight: 700; font-size: 16px; letter-spacing: 0.1em; color: var(--navy); }
  .intro-de, .intro-en { font-weight: 300; font-size: 17px; }
  .intro-de { top: 288px; color: var(--navy); }
  .intro-en { top: 310px; color: var(--lilac); }
  .name-band {
    position: absolute; left: 162px; top: 365px; width: 878px; height: 120px;
    background: repeating-linear-gradient(to bottom, var(--rule) 0 1px, transparent 1px 5.9px);
  }
  .participant { top: 383px; font-weight: 900; font-size: 88px; color: var(--ink); letter-spacing: -0.005em; }
  .caption { font-size: 11px; letter-spacing: 0.2em; color: var(--navy); font-weight: 400; }
  .caption .en { color: var(--lilac); }
  .caption-name { top: 495px; }
  .date-block { position: absolute; left: 162px; top: 660px; width: 264px; text-align: center; }
  .date-value { font-weight: 300; font-size: 23px; line-height: 1; height: 34px; border-bottom: 1px solid #777; padding-top: 3px; }
  .date-block .caption { margin-top: 8px; line-height: 1; }
  .date-block .caption .en { color: var(--blue); }
  .seal {
    position: absolute; left: 498px; top: 568px; width: 204px; height: 204px; border-radius: 50%;
    background:
      radial-gradient(circle at 50% 50%, rgba(255,255,255,0.55) 0 30%, transparent 62%),
      conic-gradient(from 200deg, #b89ad8, #e8b6d6, #b9d2ee, #a9e0ee, #c6b8ea, #9fc8ee, #f0c8d8, #b89ad8);
    box-shadow: 2px 4px 8px rgba(14,32,62,0.18);
  }
  .signatures { position: absolute; left: 775px; top: 600px; width: 265px; text-align: center; }
  .signature { font-family: "Kaushan Script", cursive; font-size: 40px; line-height: 1; color: var(--ink); height: 57px; border-bottom: 1px solid #777; padding-top: 10px; }
  .signature + .signature { height: 73px; padding-top: 25px; }
  .signatures .caption { margin-top: 8px; line-height: 1; white-space: nowrap; }
</style>
</head>
<body>
<main class="certificate">
  <svg class="frame" width="1200" height="849" viewBox="0 0 2292 1622" aria-hidden="true">
    <g fill="none" stroke="var(--frame)" stroke-width="9">
      <path d="M158,80 H2138 V133 H2190 V158 H2216 V1463 H2190 V1489 H2138 V1542 H158 V1489 H105 V1463 H80 V158 H105 V133 H158 Z"/>
      <rect x="105" y="105" width="30" height="30"/>
      <rect x="2161" y="105" width="30" height="30"/>
      <rect x="105" y="1487" width="30" height="30"/>
      <rect x="2161" y="1487" width="30" height="30"/>
    </g>
  </svg>

  <h1 class="line title-de">TEILNAHMEZERTIFIKAT</h1>
  <p class="line title-en">CERTIFICATE OF ATTENDANCE</p>

  <p class="line academy">LOGO TALWERK AKADEMIE</p>

  <p class="line intro-de">gratuliert zum erfolgreichen Abschluss</p>
  <p class="line intro-en">hereby certifies the successful completion</p>

  <div class="name-band" aria-hidden="true"></div>
  <p class="line participant">Max Mustermann</p>
  <p class="line caption caption-name">NAME / <span class="en">NAME OF PARTICIPANT</span></p>

  <div class="date-block">
    <p class="date-value">16. November 2025</p>
    <p class="caption">DATUM / <span class="en">DATE</span></p>
  </div>

  <div class="seal" role="img" aria-label="Hologramm-Siegel der Talwerk Akademie"></div>

  <div class="signatures">
    <p class="signature">L. Brandt</p>
    <p class="signature">M. Hofstetter</p>
    <p class="caption">LEITUNG / <span class="en">HEAD OF TALWERK AKADEMIE</span></p>
  </div>
</main>
</body>
</html>
```